Name of Business is Tidewell Vitality Mentor,
Business Card and Logo Design for a health coaching practice that brings together all aspects of living including breathing, meditation, heartfelt intentional living, oneness with others, compassion, nutrition, hydration and primary care physician.

Target Market(s)

People looking for holistic approach to optimal living.

Industry/Entity Type

Business

Contact Information for Business Card

Marcus R.T. Dunmore
CLP, CCHC, C-IQ
Tidewell Vitality Mentor
614 Birchmoor Ave
Cedarhaven Shores, MI 48305

Logo Text

Everything You Need Is Within You Now

```html
<!DOCTYPE html>
<html lang="en">
<head>
<meta charset="utf-8">
<title>Tidewell Vitality Mentor — Business Card</title>
<link rel="stylesheet" href="https://fonts.googleapis.com/css2?family=Source+Sans+3:wght@400&display=swap">
<style>
  :root {
    --backdrop: #333132;
    --card-front: #d0cce5;
    --brand-blue: #14a8cb;
    --brand-pink: #ef3192;
    --fold-dark: #b1b1b1;
    --fold-light: #d3d3d3;
    --ink: #1e1e24;
    --white: #ffffff;
  }
  * { margin: 0; padding: 0; box-sizing: border-box; }
  html, body {
    width: 1200px; height: 799px; overflow: hidden;
    background: var(--backdrop);
    font-family: "Source Sans 3", "Myriad Pro", Arial, sans-serif;
  }
  .stage { position: relative; width: 1200px; height: 799px; }

  .card-front {
    position: absolute; left: 364px; top: 80px;
    width: 505px; height: 305px;
    background: var(--card-front);
  }
  .brand-badge {
    position: absolute; left: 49px; top: 51px;
    width: 124px; height: 119px; border-radius: 50%;
    background: var(--brand-blue);
    display: flex; align-items: center; justify-content: center;
  }
  .brand-name {
    color: var(--white); font-size: 17px; font-weight: 400; letter-spacing: 0.3px;
  }
  .contact {
    position: absolute; left: 286px; top: 126px;
    color: var(--ink); line-height: 1;
  }
  .contact-name { font-size: 16.5px; margin-bottom: 10px; }
  .contact-credentials { font-size: 11.5px; margin-bottom: 12px; }
  .contact-line { font-size: 12.5px; line-height: 15.8px; }

  .card-back {
    position: absolute; left: 361px; top: 423px;
    width: 505px; height: 304px; display: block;
  }
  .back-brand-name {
    font-family: "Source Sans 3", "Myriad Pro", Arial, sans-serif;
    font-size: 26px; fill: var(--white);
  }
</style>
</head>
<body>
<main class="stage">
  <section class="card-front" aria-label="Business card front">
    <div class="brand-badge"><span class="brand-name">Tidewell</span></div>
    <div class="contact">
      <p class="contact-name">Marcus R.T. Dunmore</p>
      <p class="contact-credentials">CLP, CCHC, C-IQ</p>
      <p class="contact-line">Tidewell Vitality Mentor</p>
      <p class="contact-line">614 Birchmoor Ave</p>
      <p class="contact-line">Cedarhaven Shores, MI 48305</p>
      <p class="contact-line">Ph:+00......</p>
      <p class="contact-line">E:urid@domain.com</p>
    </div>
  </section>

  <svg class="card-back" viewBox="0 0 505 304" aria-label="Business card back">
    <rect class="back-field" width="505" height="304" fill="var(--brand-pink)"/>
    <polygon class="fold-shadow" points="505,0 199,304 302,304" fill="var(--fold-dark)"/>
    <polygon class="fold-face" points="505,0 302,304 505,304" fill="var(--fold-light)"/>
    <text class="back-brand-name" x="237" y="114" text-anchor="middle">Tidewell</text>
  </svg>
</main>
</body>
</html>
```